UNDER ONE [BRIGHT] LANTERN, Shape your path

We are looking for a cover refresh of an existing bestselling book that is going into 3rd edition print this year.
The book is an inspirational as well as educational book that has become recognized as one of the most comprehensive, actionable, personal and financial planning resources available today for families, individuals and business owners alike.
Comprised of three true stories of loss, learning to live and love again and a 30 page checklist at the back of the book it contains tips and strategies for everyone to help them to get their personal and financial lives in order while they can.
The cover must have the following:
1. Appeal to a broad audience/both personal and corporate
2. Include Mira Tollenkamp Bestselling Author
3. Include introduction of a new Afterword
4. 3rd Edition
5. Colors to remain the same – red, black and white
6. The title must remain in caps and the word [BRIGHT] must have the brackets around it
We have also added a current copy of the second edition to help you. For your information our website is www.thetollenkampcircle.example
Reason: We have narrowed it down to our top 3 designs. We are submitting the covers to our community for them to pick the top cover. Good luck to everyone

```html
<!DOCTYPE html>
<html lang="en">
<head>
<meta charset="utf-8">
<title>Under One [Bright] Lantern — Cover</title>
<link href="https://fonts.googleapis.com/css2?family=Rye&family=Smokum&family=Oswald:wght@400;500&family=Great+Vibes&display=swap" rel="stylesheet">
<style>
  :root {
    --backdrop: #dcd9de;
    --cover-black: #0c0c0d;
    --title-red: #d3141b;
    --title-red-dark: #7e0a0e;
    --band-red: #c8161c;
    --band-red-deep: #a50f14;
    --silver-light: #f2f2f2;
    --silver-dark: #7d7d80;
    --white: #ffffff;
  }
  html, body {
    margin: 0;
    width: 1200px;
    height: 1054px;
    overflow: hidden;
    background: var(--backdrop);
  }
  .cover-frame {
    position: absolute;
    left: 235px;
    top: 20px;
    width: 760px;
    height: 1055px;
    transform: scale(0.961);
    transform-origin: 0 0;
  }
  .cover {
    position: relative;
    width: 760px;
    height: 1055px;
    background: radial-gradient(ellipse at 50% 35%, #242426 0%, var(--cover-black) 70%);
    overflow: hidden;
    box-shadow: 0 6px 18px rgba(0,0,0,0.25);
  }
  .cover-photo {
    position: absolute;
    left: 0;
    top: 530px;
    width: 760px;
    height: 420px;
    background:
      radial-gradient(ellipse at 48% 55%, rgba(215,190,175,0.55) 0%, rgba(120,110,105,0.25) 30%, rgba(0,0,0,0) 60%),
      linear-gradient(180deg, #0c0c0d 0%, #2a2a2c 55%, #e8e8e8 82%, #1a1a1b 88%, #050505 100%);
  }
  .edition-corner {
    position: absolute;
    inset: 0;
  }
  .title-block {
    position: absolute;
    left: 0;
    top: 0;
  }
  .title-small {
    font-family: "Rye", serif;
    fill: url(#silver);
  }
  .title-main {
    font-family: "Smokum", serif;
    fill: url(#redface);
    stroke: var(--title-red-dark);
    stroke-width: 2;
  }
  .tagline {
    font-family: "Great Vibes", cursive;
    fill: var(--white);
  }
  .edition-label {
    font-family: "Oswald", sans-serif;
    font-weight: 500;
    fill: var(--white);
  }
  .author-band {
    position: absolute;
    left: 0;
    top: 947px;
    width: 760px;
    height: 72px;
    background: linear-gradient(180deg, var(--band-red) 0%, var(--band-red-deep) 100%);
    display: flex;
    justify-content: center;
    align-items: center;
  }
  .author-name {
    width: 310px;
    height: 72px;
    background: var(--band-red-deep);
    color: var(--white);
    font-family: "Oswald", sans-serif;
    font-weight: 400;
    font-size: 38px;
    letter-spacing: 2px;
    text-transform: uppercase;
    display: flex;
    justify-content: center;
    align-items: center;
    margin: 0;
    white-space: nowrap;
  }
</style>
</head>
<body>
  <div class="cover-frame">
    <section class="cover">
      <div class="cover-photo" role="img" aria-label="Photograph of a hand in a dark suit sleeve signing a sheet of paper with a fountain pen on a glossy black desk"></div>

      <svg class="title-block" width="760" height="1055" viewBox="0 0 760 1055">
        <defs>
          <linearGradient id="silver" x1="0" y1="0" x2="0" y2="1">
            <stop offset="0" stop-color="var(--silver-light)"/>
            <stop offset="0.55" stop-color="#b8b8ba"/>
            <stop offset="1" stop-color="var(--silver-dark)"/>
          </linearGradient>
          <linearGradient id="redface" x1="0" y1="0" x2="0" y2="1">
            <stop offset="0" stop-color="#ff3a3f"/>
            <stop offset="0.5" stop-color="var(--title-red)"/>
            <stop offset="1" stop-color="#9b0d12"/>
          </linearGradient>
          <linearGradient id="bracket" x1="0" y1="0" x2="1" y2="0">
            <stop offset="0" stop-color="#5e5e60"/>
            <stop offset="0.5" stop-color="#d9d9db"/>
            <stop offset="1" stop-color="#6a6a6c"/>
          </linearGradient>
        </defs>

        <!-- edition corner ribbon -->
        <polygon points="578,0 660,0 760,100 760,172" fill="var(--band-red)"/>
        <text class="edition-label" x="0" y="0" font-size="34" text-anchor="middle"
              transform="translate(688,92) rotate(45)">3RD EDITION</text>
        <text class="edition-label" x="0" y="0" font-size="16" text-anchor="middle"
              transform="translate(720,38) rotate(45)">NEW!</text>

        <!-- brackets -->
        <path d="M108 176 H60 V412 H108" fill="none" stroke="url(#bracket)" stroke-width="11"/>
        <path d="M652 176 H698 V412 H652" fill="none" stroke="url(#bracket)" stroke-width="11"/>

        <!-- title -->
        <text class="title-small" x="112" y="194" font-size="50" textLength="258" lengthAdjust="spacingAndGlyphs">UNDER ONE</text>
        <text class="title-main" x="110" y="385" font-size="222" textLength="548" lengthAdjust="spacingAndGlyphs">BRIGHT</text>
        <text class="title-small" x="380" y="449" font-size="50" textLength="258" lengthAdjust="spacingAndGlyphs">LANTERN</text>

        <!-- tagline band -->
        <g transform="translate(385,500) rotate(8)">
          <rect x="-125" y="-28" width="250" height="56" fill="none" stroke="var(--title-red)" stroke-width="2"/>
          <text class="tagline" x="0" y="10" font-size="34" text-anchor="middle">Shape your path</text>
        </g>
      </svg>

      <div class="author-band">
        <h2 class="author-name">Mira Tollenkamp</h2>
      </div>
    </section>
  </div>
</body>
</html>
```